Print and E-book Personal Injury Front and Back Book Cover

I need a book cover for a personal injury law firm book titled "Rising Past the Wreckage" with the subtitle "A Plain Guide for Harmed Readers." The book cover should have an image. This isas a lead generation book designed to be give to potential clients to have them sign as new clients.

Target Market(s)

Potential New Clients Looking For a Personal Injury Attorney

Industry/Entity Type

Legal

Requirements
Must have
• Title and some type of image or images

```html
<!DOCTYPE html>
<html lang="en">
<head>
<meta charset="utf-8">
<title>Rising Past the Wreckage – Book Cover</title>
<link rel="stylesheet" href="https://fonts.googleapis.com/css2?family=Barlow+Semi+Condensed:wght@700;800&display=swap">
<style>
  :root {
    --stage: #e9e8e4;
    --navy: #1b3a52;
    --gold: #fbb416;
    --white: #ffffff;
    --slate-dark: #2b3137;
    --slate-mid: #5d646a;
    --slate-light: #8a9095;
  }
  * { margin: 0; padding: 0; box-sizing: border-box; }
  html, body {
    width: 1200px;
    height: 792px;
    overflow: hidden;
    background: var(--stage);
  }
  .stage {
    width: 1200px;
    height: 792px;
    display: flex;
    align-items: center;
    justify-content: center;
  }
  .book-cover {
    width: 480px;
    height: 720px;
    background: var(--navy);
    display: flex;
    flex-direction: column;
    box-shadow: 0 10px 30px rgba(0, 0, 0, 0.18);
    font-family: "Barlow Semi Condensed", "Arial Narrow", sans-serif;
  }
  .cover-type {
    height: 432px;
    display: flex;
    flex-direction: column;
    align-items: center;
    padding-top: 78px;
    text-align: center;
  }
  .book-title {
    color: var(--gold);
    font-weight: 800;
    font-size: 64px;
    line-height: 0.9;
    letter-spacing: 0.5px;
    text-transform: uppercase;
  }
  .book-subtitle {
    margin-top: 44px;
    color: var(--white);
    text-transform: uppercase;
    font-weight: 700;
  }
  .subtitle-lead {
    display: block;
    font-size: 38px;
    line-height: 1;
    letter-spacing: 0.3px;
  }
  .subtitle-rest {
    display: block;
    font-size: 19px;
    line-height: 1.1;
    margin-top: 2px;
    letter-spacing: 0.2px;
  }
  .cover-image {
    flex: 1;
    border-top: 1px solid rgba(251, 180, 22, 0.35);
    background:
      radial-gradient(ellipse at 50% 45%, var(--slate-light) 0%, var(--slate-mid) 45%, var(--slate-dark) 100%);
  }
</style>
</head>
<body>
  <main class="stage">
    <article class="book-cover">
      <header class="cover-type">
        <h1 class="book-title">Rising Past<br>the Wreckage</h1>
        <p class="book-subtitle">
          <span class="subtitle-lead">A Plain Guide</span>
          <span class="subtitle-rest">for Harmed Readers</span>
        </p>
      </header>
      <div class="cover-image" role="img" aria-label="Photograph of a hand holding a dark wooden judge's gavel with a brass band against a textured grey wall"></div>
    </article>
  </main>
</body>
</html>
```